Therapist website

I need a sqaure space web design for my therapy practice. I need a home page, a services page with 4 subpages, an about me, an insurnace page, a contact page, an EMDR page

```html
<!DOCTYPE html>
<html lang="en">
<head>
<meta charset="utf-8">
<title>Willowbend Family Counseling</title>
<link rel="stylesheet" href="https://fonts.googleapis.com/css2?family=Arimo:wght@400;700&display=swap">
<style>
:root{
  --teal:#12b5ba;
  --teal-dark:#1a9aa0;
  --teal-grad:linear-gradient(90deg,#1a9ca2,#0bc2c4);
  --ink:#1b1b1b;
  --muted:#555;
  --white:#fff;
  --bar:#ececec;
}
*{margin:0;padding:0;box-sizing:border-box}
html,body{width:1200px;height:1200px;overflow:hidden;background:var(--white)}
body{font-family:"Arimo",Arial,sans-serif;color:var(--ink)}
.page{position:absolute;left:360px;top:0;width:480px;height:1200px;background:var(--white)}
.abs{position:absolute}

/* hero */
.hero{left:0;top:0;width:480px;height:232px;background:linear-gradient(180deg,#4f6d86 0%,#7f8a7c 35%,#a88b56 65%,#8f6c3a 100%)}
.hero-shade{left:0;top:0;width:480px;height:232px;background:rgba(20,30,40,.25)}
.logo{left:16px;top:0;width:58px;height:37px;background:var(--white);display:flex;align-items:center;justify-content:center;gap:3px}
.logo-dot{width:5px;height:5px;border-radius:50%;background:var(--teal)}
.logo-name{font-size:6px;font-weight:700;color:var(--teal-dark);letter-spacing:.3px}
.nav a{position:absolute;top:17px;font-size:5px;letter-spacing:1.6px;color:var(--white);text-decoration:none}
.nav .active::after{content:"";position:absolute;left:-1px;right:0;top:7px;height:1.5px;background:var(--teal)}
.nav-cta{left:395px;top:12px;width:60px;height:16px;border-radius:8px;background:var(--teal);color:var(--white);font-size:5px;display:flex;align-items:center;justify-content:center}
.hero-kicker{left:0;width:480px;top:84px;text-align:center;font-size:6px;letter-spacing:2px;color:var(--white)}
.hero-title{left:0;width:480px;top:94px;text-align:center;font-size:16px;color:var(--white)}
.hero-text{left:140px;width:200px;top:118px;text-align:center;font-size:4.2px;line-height:7px;color:var(--white)}
.hero-btn{left:200px;top:144px;width:79px;height:15px;border:1px solid var(--white);border-radius:8px;color:var(--white);font-size:5px;display:flex;align-items:center;justify-content:center}

/* band */
.band{left:0;top:232px;width:480px;height:46px;background:var(--teal-grad)}
.band-text{left:74px;top:247px;font-size:12px;color:var(--white)}
.band-btn{left:301px;top:246px;width:104px;height:18px;border-radius:9px;background:var(--white);color:var(--teal-dark);font-size:4.6px;display:flex;align-items:center;justify-content:center}

/* cards */
.photo{border-radius:0}
.card{background:var(--white);box-shadow:0 3px 14px rgba(0,0,0,.12);padding:36px 0 0 33px}
.card h2{font-size:16px;font-weight:400;color:var(--ink)}
.card h2 .accent{color:var(--teal);font-weight:700}
.card p{margin-top:12px;width:180px;font-size:4.6px;line-height:8.6px;color:var(--ink)}
.pill{display:inline-flex;align-items:center;justify-content:center;width:59px;height:15px;border-radius:8px;background:var(--teal-dark);color:var(--white);font-size:4.6px;margin-top:11px}
.card-dot{width:3px;height:3px;border-radius:50%;background:var(--teal)}

/* services */
.services-title{left:0;width:480px;top:579px;text-align:center;font-size:16px}
.services-title .accent{color:var(--teal);font-weight:700}
.services-intro{left:80px;width:320px;top:608px;text-align:center;font-size:4.6px;line-height:8.6px}
.service{width:100px;top:638px;text-align:center}
.service .icon{width:72px;height:72px;border-radius:50%;background:var(--teal-grad);margin:0 auto;display:flex;align-items:center;justify-content:center}
.service h3{margin-top:14px;font-size:7px;color:var(--teal-dark)}
.service p{margin-top:5px;font-size:4.4px;line-height:8.4px;color:var(--muted)}
.service .more{margin-top:4px;font-size:5px;font-weight:700;color:var(--teal)}

/* footer */
.foot h4{font-size:7.4px;font-weight:700}
.foot p,.foot li{font-size:4.6px;line-height:8.8px;color:var(--ink);list-style:none}
.foot .head-gap{margin-top:8px}
.contact-row{display:flex;align-items:center;gap:5px}
.socials{display:flex;gap:3px;margin-top:6px}
.socials span{width:9px;height:9px;border-radius:50%;background:#3c6ab3}
.socials span:nth-child(2){background:#3aa3e3}
.socials span:nth-child(3){background:#1d74b0}
.socials span:nth-child(4){background:#d6443a}
.copyright{left:0;top:1179px;width:480px;height:21px;background:var(--bar);font-size:4.6px;display:flex;align-items:center;justify-content:center}
</style>
</head>
<body>
<div class="page">

  <div class="abs hero" role="img" aria-label="Photo of two young women walking through a golden wheat field under a blue sky"></div>
  <div class="abs hero-shade"></div>
  <div class="abs logo"><span class="logo-dot"></span><span class="logo-name">WILLOWBEND</span></div>
  <nav class="nav">
    <a class="active" style="left:184px">HOME</a>
    <a style="left:226px">ABOUT ME</a>
    <a style="left:290px">INSURNACE</a>
    <a style="left:358px">EMDR</a>
  </nav>
  <div class="abs nav-cta">CONTACT US</div>
  <div class="abs hero-kicker">WELCOME TO</div>
  <div class="abs hero-title">WILLOWBEND</div>
  <div class="abs hero-text">Holisticly build progressive e-markets without long-term high-impact e-tailers. Intrinsicly e-enable cross-unit quality vectors without team building ROI.</div>
  <div class="abs hero-btn">CONTACT US</div>

  <div class="abs band"></div>
  <div class="abs band-text">Don't Wait to Get the Help You Need</div>
  <div class="abs band-btn">BOOK AN APPOINTMENT</div>

  <div class="abs photo" style="left:200px;top:276px;width:260px;height:274px;background:linear-gradient(160deg,#c98a2e 0%,#6f7a3a 45%,#2f3a22 100%)" role="img" aria-label="Photo of a smiling family of three outdoors among autumn trees"></div>
  <div class="abs card" style="left:15px;top:347px;width:224px;height:178px">
    <h2><span class="accent">About</span> Me</h2>
    <div class="abs card-dot" style="left:125px;top:52px"></div>
    <p>Progressively fabricate enterprise-wide catalysts for change and high standards in testing procedures. Authoritatively re-engineer cooperative infrastructures for interdependent best practices. Objectively morph prospective content and turnkey mindshare. Dynamically embrace scalable communities whereas flexible solutions. Appropriately create superior e-commerce whereas bleeding-edge growth strategies.</p>
    <span class="pill">LEARN MORE</span>
  </div>

  <div class="abs services-title">Our <span class="accent">Services</span></div>
  <div class="abs services-intro">Progressively fabricate enterprise-wide catalysts for change and high standards in testing procedures. Authoritatively re-engineer cooperative infrastructures for interdependent best practices.</div>

  <div class="abs service" style="left:28px">
    <div class="icon"><svg width="22" height="22" viewBox="0 0 22 22" fill="none" stroke="#fff" stroke-width="1.6" stroke-linecap="round"><circle cx="11" cy="4" r="2.4" fill="#fff" stroke="none"/><path d="M6 10l5-2 5 2M11 8v6M8 19l3-5 3 5M6 14h10"/></svg></div>
    <h3>Child and Adolescent</h3>
    <p>Progressively fabricate wide catalysts<br>for change fabricate</p>
    <div class="more">Learn More →</div>
  </div>
  <div class="abs service" style="left:136px">
    <div class="icon"><svg width="22" height="22" viewBox="0 0 22 22" fill="none" stroke="#fff" stroke-width="1.5" stroke-linecap="round"><path d="M6 9a5 6 0 0 1 10 0v3a5 5 0 0 1-10 0z"/><path d="M6 9c3 0 6-1 7-3"/><path d="M8 19l3 2 3-2"/></svg></div>
    <h3>Adult</h3>
    <p>Progressively fabricate wide catalysts<br>for change fabricate</p>
    <div class="more">Learn More →</div>
  </div>
  <div class="abs service" style="left:244px">
    <div class="icon"><svg width="24" height="22" viewBox="0 0 24 22" fill="none" stroke="#fff" stroke-width="1.6" stroke-linecap="round"><path d="M6 3v9h8l2 4M6 12l-1 4h12"/><circle cx="7" cy="18" r="2"/><circle cx="18" cy="18" r="2"/></svg></div>
    <h3>Special Needs Parenting</h3>
    <p>Progressively fabricate wide catalysts<br>for change fabricate</p>
    <div class="more">Learn More →</div>
  </div>
  <div class="abs service" style="left:346px">
    <div class="icon"><svg width="24" height="22" viewBox="0 0 24 22" fill="none" stroke="#fff" stroke-width="1.6" stroke-linejoin="round"><path d="M12 3l4 2v4l-4 2-4-2V5z" fill="#fff"/><path d="M3 8v6l5 5M21 8v6l-5 5M6 12l3 3M18 12l-3 3"/></svg></div>
    <h3>Foster Care and Adoption</h3>
    <p>Progressively fabricate wide catalysts<br>for change fabricate</p>
    <div class="more">Learn More →</div>
  </div>

  <div class="abs photo" style="left:0;top:795px;width:253px;height:274px;background:linear-gradient(150deg,#c9a27a 0%,#b08458 45%,#8a6a3a 100%)" role="img" aria-label="Photo of an adult hand holding a child's hand"></div>
  <div class="abs card" style="left:207px;top:844px;width:224px;height:178px">
    <h2><span class="accent">Insurance</span></h2>
    <p>Progressively fabricate enterprise-wide catalysts for change and high standards in testing procedures. Authoritatively re-engineer cooperative infrastructures for interdependent best practices. Objectively morph prospective content and turnkey mindshare. Dynamically embrace scalable communities whereas flexible solutions. Appropriately create superior e-commerce whereas bleeding-edge growth strategies.</p>
    <span class="pill">LEARN MORE</span>
  </div>

  <footer class="foot">
    <div class="abs" style="left:69px;top:1093px;width:115px">
      <h4>About Us</h4>
      <p class="head-gap">Progressively fabricate enterprise-wide catalysts for change and high standards in testing procedures. Authoritatively re-engineer cooperative infrastructures for interdependent best practices.</p>
    </div>
    <div class="abs" style="left:230px;top:1093px">
      <h4>Quick Links</h4>
      <ul class="head-gap"><li>Home</li><li>About me</li><li>Insurnace</li><li>EMDR</li><li>Contact us</li></ul>
    </div>
    <div class="abs" style="left:322px;top:1093px">
      <h4>Contact Details</h4>
      <div class="head-gap">
        <p class="contact-row"><svg width="5" height="5" viewBox="0 0 10 10"><path d="M2 1l2 2-1 1.5a6 6 0 0 0 2.5 2.5L7 6l2 2-1.5 1.5C4 9 1 6 .5 2.5z" fill="#333"/></svg>1234 567 890</p>
        <p class="contact-row"><svg width="5" height="5" viewBox="0 0 10 10"><rect x="0" y="2" width="10" height="6" fill="#333"/><path d="M0 2l5 3 5-3" stroke="#fff" fill="none"/></svg>info@email.com</p>
        <p class="contact-row"><svg width="5" height="5" viewBox="0 0 10 10"><path d="M5 0a3 3 0 0 1 3 3c0 2-3 5-3 5S2 5 2 3a3 3 0 0 1 3-3z" fill="#333"/></svg>123 street abc road Florida USA</p>
      </div>
      <div class="socials"><span></span><span></span><span></span><span></span></div>
    </div>
  </footer>

  <div class="abs copyright">© Willowbend 2017-2018. All rights reserved.</div>
</div>
</body>
</html>
```